Futuristic but clean CD Cover Design

I need a CD Cover design for my next EP. The music is electronic pop. I am looking for something clean but futuristic with neon colors .Name of band: peopleASponiesName of Album: CeylonI have attached my logo.I have also attached CD covers of the color scheme and clean look I am looking for.Thanks

Industry/Entity Type

Film Production

Requirements
Must have
• A clean future look. The music is electronic pop.

```html
<!DOCTYPE html>
<html lang="en">
<head>
<meta charset="utf-8">
<title>lanternsokites – Varmel</title>
<link rel="stylesheet" href="https://fonts.googleapis.com/css2?family=Orbitron:wght@400&family=Questrial&display=swap">
<style>
  :root {
    --deep-blue: #1a1aa8;
    --violet: #5a2fc4;
    --magenta: #e0309a;
    --flame-orange: #ff8a1e;
    --flame-yellow: #ffd21a;
    --glow-cream: #fff6d6;
    --paper-white: #fffdf5;
    --ink: #111111;
  }
  html, body {
    margin: 0;
    padding: 0;
    overflow: hidden;
    background: var(--paper-white);
  }
  .cover {
    position: relative;
    width: 1176px;
    height: 1200px;
    overflow: hidden;
    background: var(--paper-white);
  }
  .cover-artwork {
    position: absolute;
    inset: 0;
    background:
      radial-gradient(ellipse 420px 520px at 50% 45%, rgba(255, 210, 26, 0.55), rgba(224, 48, 154, 0.35) 55%, transparent 80%),
      radial-gradient(ellipse 380px 300px at 14% 42%, rgba(40, 60, 200, 0.9), transparent 75%),
      linear-gradient(180deg,
        var(--deep-blue) 0%,
        var(--deep-blue) 22%,
        var(--violet) 40%,
        var(--magenta) 55%,
        var(--flame-orange) 66%,
        var(--flame-yellow) 74%,
        var(--glow-cream) 84%,
        var(--paper-white) 92%);
  }
  .band-name {
    position: absolute;
    left: 118px;
    top: 1000px;
    width: 940px;
    margin: 0;
    font-family: "Questrial", sans-serif;
    font-weight: 400;
    font-size: 112px;
    line-height: 130px;
    letter-spacing: 1px;
    color: var(--ink);
    text-align: center;
    white-space: nowrap;
  }
  .album-title {
    position: absolute;
    left: 198px;
    top: 1136px;
    width: 730px;
    margin: 0;
    display: flex;
    justify-content: space-between;
    font-family: "Orbitron", sans-serif;
    font-weight: 400;
    font-size: 52px;
    line-height: 60px;
    color: var(--ink);
  }
</style>
</head>
<body>
  <main class="cover">
    <div class="cover-artwork" role="img" aria-label="Neon illustration of a rearing horse dissolving into swirling magenta, yellow and white flames against a deep blue sky"></div>
    <h1 class="band-name">lanternsokites</h1>
    <h2 class="album-title" aria-label="Varmel">
      <span>V</span><span>a</span><span>r</span><span>m</span><span>e</span><span>l</span>
    </h2>
  </main>
</body>
</html>
```